Ridgemont Business Card Redesign

Using the current logo/tagline lock-up and icon, redesign the Ridgemont business card to better show the tagline and improve the layout to give the card a more timely design and a classic, sophisticated look. See attached Project Brief for more detail.

```html
<!DOCTYPE html>
<html lang="en">
<head>
<meta charset="utf-8">
<title>Ridgemont Capital – Business Card</title>
<link rel="stylesheet" href="https://fonts.googleapis.com/css2?family=Marcellus&family=Marcellus+SC&display=swap">
<style>
  :root {
    --page: #ffffff;
    --ink: #111111;
    --brand-blue: #1f74c0;
    --card-light: #ffffff;
    --card-mid: #e6e6e6;
    --card-dark: #b9b9b9;
  }
  html, body {
    margin: 0;
    width: 1200px;
    height: 1200px;
    overflow: hidden;
    background: var(--page);
  }
  .card {
    position: absolute;
    left: 179px;
    top: 101px;
    width: 838px;
    height: 480px;
    background:
      radial-gradient(ellipse 70% 85% at 38% 62%, var(--card-light) 0%, var(--card-mid) 55%, var(--card-dark) 100%);
    color: var(--ink);
    font-family: "Marcellus SC", serif;
  }
  .card > * { position: absolute; margin: 0; line-height: 1; white-space: nowrap; }

  .brand-mark {
    left: 95px;
    top: 57px;
    width: 126px;
    height: 126px;
    border-radius: 50%;
    background: var(--brand-blue);
  }
  .brand-name {
    left: 230px;
    width: 460px;
    text-align: center;
    top: 24px;
    font-family: "Marcellus", serif;
    font-size: 74px;
    letter-spacing: -1px;
    color: var(--ink);
  }
  .brand-sub {
    left: 230px;
    width: 466px;
    text-align: center;
    top: 104px;
    font-family: "Marcellus", serif;
    font-size: 56px;
    letter-spacing: 18px;
    color: var(--brand-blue);
  }
  .tagline {
    left: 233px;
    width: 500px;
    text-align: center;
    top: 150px;
    font-size: 33px;
    font-weight: 400;
    color: var(--ink);
    text-shadow: 1px 1px 0 rgba(0,0,0,0.35);
  }

  .person { left: 0; width: 838px; text-align: center; }
  .person-name { top: 231px; font-size: 33px; color: var(--brand-blue); left: 62px; }
  .person-role { top: 262px; font-size: 26px; left: 26px; }
  .person-title { top: 296px; font-size: 26px; left: 26px; }

  .address { left: 27px; top: 352px; font-size: 27px; line-height: 30px; }
  .phones  { left: 525px; top: 352px; font-size: 27px; line-height: 30px; }
  .email {
    left: 27px;
    top: 447px;
    font-family: "Marcellus", serif;
    font-size: 27px;
    letter-spacing: 11.4px;
    color: var(--brand-blue);
  }
</style>
</head>
<body>
  <section class="card" aria-label="Ridgemont Capital business card">
    <div class="brand-mark" aria-hidden="true"></div>
    <h1 class="brand-name">RIDGEMONT</h1>
    <p class="brand-sub">CAPITAL</p>
    <p class="tagline">Non-Control Growth Capital</p>

    <p class="person person-name">Daniel R. Whitcombe</p>
    <p class="person person-role">Pricipal &amp;</p>
    <p class="person person-title">Chief Marketing Officer</p>

    <address class="address" style="font-style:normal">
      47 Alder Crest Road<br>
      Suite 210<br>
      Fairbrook, Ct. 06599
    </address>
    <p class="phones">
      Office : (555) 210-4837<br>
      Cell :&nbsp;&nbsp; (555) 318-6092
    </p>
    <p class="email">dwhitcombe@ridgemontcapital.com</p>
  </section>
</body>
</html>
```